Business Card Design Project

We are launching a new business for developing and running an SaaS (cloud-based applications service) in China. Our products are business applications that enable mid-size retailors to run their service operation and customer management in pay-as-you-go basis.

Tellova stands for our mission to enable our clients run business wiser. The Chinese name is 禾联达, that means 数字平台携手经营添新彩.

Our slogan is help your trade flow brighter, 携手经营添新彩.

Key Words to describe our business:
- International/Global product innovation
- Cloud-based business applications services
- Pay-as-you-go
- Mid-market in China

This task is to design our business card system in English/Chinese combination.
Updates

Project Deadline Extended
Reason: Since I'm out of office for a week, hope this deadline extending can help you have more time for new submissions and changes.

Target Market(s)

Mid-size business customers for retail and consumer services industry in China

Industry/Entity Type

Business

Requirements
Must have
• Double-side design: One side is in Chinese and another side in English. Each of side will include all contents as follows

1. Highlight our 3 business offerings: growth strategy,operation improvement and CRM-as-a-Service
and in Chinese: 增长战略 . 运营优化 . 营销管理软件云服务

2. Include elements: Logo with slogan, Name, job title, Mobile, e-mail, company name and web site, Linkedin profile URL.

3. Include QR code for business card for above information in English or Chinese

Plastic (PVC) Business Card Printing need be supported by the design.

Provide a completed template with a sample as following:

Name: Ruan Kevin 欧阳莉
Title: Product Manager 产品经理
Mobile: +86-1592-8406-713
E-mail: kevin.ruan@tellova-demo.net
Linkedin Profile: cn.prolinkhub-demo.com/in/kevinruan

Company name: Tellova (Shenzhen) Inc. 深圳市禾联达科技有限公司
Web site: www.tellova-demo.net

Nice to have
• The design not ordinary

```html
<!DOCTYPE html>
<html lang="en">
<head>
<meta charset="utf-8">
<title>Tellova Business Card</title>
<link rel="stylesheet" href="https://fonts.googleapis.com/css2?family=Ubuntu:wght@400;500;700&family=Noto+Sans+SC:wght@400;500&display=swap">
<style>
  :root {
    --page-bg: #d9d6d1;
    --card-frost: #e9ebec;
    --card-edge: #f6f7f7;
    --navy: #0b3459;
    --cyan: #17c1f2;
    --slate: #909498;
    --white: #ffffff;
    --rule: #8fa3b5;
  }
  * { box-sizing: border-box; margin: 0; padding: 0; }
  html, body {
    width: 1200px; height: 1000px; overflow: hidden;
    background: var(--page-bg);
    font-family: "Ubuntu", sans-serif;
  }
  .canvas { position: relative; width: 1200px; height: 1000px; }

  .card {
    position: absolute; left: 125px; top: 236px;
    width: 950px; height: 528px;
    background: var(--card-frost);
    border: 2px solid var(--card-edge);
    border-radius: 22px;
    box-shadow: 0 10px 30px rgba(0,0,0,0.12);
    overflow: hidden;
  }

  .brand-disc {
    position: absolute; left: 32px; top: 33px;
    width: 408px; height: 462px;
    background: var(--white);
    border-radius: 231px 0 0 231px / 231px 0 0 231px;
    display: flex; align-items: center; justify-content: center;
    padding-left: 30px;
  }
  .brand-disc .brand-name {
    font-weight: 700; font-size: 78px; color: var(--cyan);
    letter-spacing: 1px;
  }

  .masthead {
    position: absolute; left: 473px; top: 33px;
    width: 475px; height: 143px;
    background: var(--navy);
    padding: 18px 0 0 42px;
  }
  .masthead .wordmark {
    font-weight: 700; font-size: 76px; line-height: 1;
    color: var(--white); letter-spacing: 1px; text-transform: uppercase;
  }
  .masthead .cn-row {
    display: flex; align-items: center; gap: 14px; margin-top: 6px;
  }
  .masthead .cn-row .rule {
    width: 236px; height: 2px; background: var(--rule);
  }
  .masthead .cn-name {
    font-family: "Noto Sans SC", sans-serif; font-weight: 400;
    font-size: 32px; color: var(--white); letter-spacing: 4px; line-height: 1;
  }

  .offerings {
    position: absolute; left: 473px; top: 186px;
    width: 475px; height: 92px;
    background: var(--slate);
    padding: 10px 0 0 42px;
    list-style: none;
  }
  .offerings li {
    font-weight: 500; font-size: 19px; line-height: 25px;
    color: var(--white); letter-spacing: 0.6px;
  }

  .contact-panel {
    position: absolute; left: 473px; top: 286px;
    width: 475px; height: 242px;
    background: var(--cyan);
    border-radius: 0 0 20px 0;
    padding: 20px 0 0 42px;
    color: var(--navy);
  }
  .person-name {
    font-weight: 700; font-size: 33px; letter-spacing: 1px; line-height: 1.1;
  }
  .person-title {
    font-weight: 500; font-size: 19px; color: var(--white);
    letter-spacing: 0.6px; margin-top: 4px;
  }
  .contact-list { list-style: none; margin-top: 12px; }
  .contact-list li {
    display: flex; align-items: center; gap: 6px;
    font-weight: 500; font-size: 21px; line-height: 29px; letter-spacing: 0.4px;
    white-space: nowrap;
  }
  .contact-list .small { font-size: 18px; letter-spacing: 0; }
  .icon { width: 20px; height: 20px; flex: none; }
</style>
</head>
<body>
<div class="canvas">
  <div class="card">
    <div class="brand-disc">
      <span class="brand-name">Tellova</span>
    </div>

    <header class="masthead">
      <div class="wordmark">Tellova</div>
      <div class="cn-row">
        <span class="rule"></span>
        <span class="cn-name">禾联达</span>
      </div>
    </header>

    <ul class="offerings">
      <li>Growth Strategy</li>
      <li>Operational Improvement</li>
      <li>Software-as-a-service</li>
    </ul>

    <section class="contact-panel">
      <div class="person-name">Ruan Kevin</div>
      <div class="person-title">Product Manager</div>
      <ul class="contact-list">
        <li>
          <svg class="icon" viewBox="0 0 20 20" aria-hidden="true">
            <rect width="20" height="20" rx="4" fill="#fff"/>
            <rect x="6.5" y="3" width="7" height="14" rx="1.5" fill="none" stroke="#17c1f2" stroke-width="1.6"/>
            <circle cx="10" cy="14.5" r="0.9" fill="#17c1f2"/>
          </svg>
          +86-1592-8406-713
        </li>
        <li>
          <svg class="icon" viewBox="0 0 20 20" aria-hidden="true">
            <rect width="20" height="20" rx="4" fill="#fff"/>
            <rect x="3.5" y="5.5" width="13" height="9" rx="1" fill="none" stroke="#17c1f2" stroke-width="1.5"/>
            <path d="M3.8 6 L10 11 L16.2 6" fill="none" stroke="#17c1f2" stroke-width="1.5"/>
          </svg>
          kevin.ruan@tellova-demo.net
        </li>
        <li class="small">
          <svg class="icon" viewBox="0 0 20 20" aria-hidden="true">
            <rect width="20" height="20" rx="4" fill="#fff"/>
          </svg>
          cn.prolinkhub-demo.com/in/kevinruan
        </li>
        <li>
          <svg class="icon" viewBox="0 0 20 20" aria-hidden="true">
            <rect width="20" height="20" rx="4" fill="#fff"/>
            <circle cx="10" cy="10" r="6" fill="none" stroke="#17c1f2" stroke-width="1.4"/>
            <ellipse cx="10" cy="10" rx="2.6" ry="6" fill="none" stroke="#17c1f2" stroke-width="1.2"/>
            <path d="M4 10 H16" stroke="#17c1f2" stroke-width="1.2"/>
          </svg>
          www.tellova-demo.net
        </li>
      </ul>
    </section>
  </div>
</div>
</body>
</html>
```